Carpentry and Building Business Card

I'm looking for a business card that is minimalistic and that incorporates the theme of my Velmor logo.
On one side I'd like the VELMOR logo with my details on the other side.
Double sided with curved edges

Target Market(s)

Construction / renovation
Adults

Industry/Entity Type

Tradesman

Contact Information for Business Card

Logo on one side, details on the other

Colors

Designer to choose only greyscale colors for use in the design.

Requirements
Must have
• Nilo Petrakis
VELMOR CONSTRUCT
Carpentry & Building Services
0481236574
Velmorconstruct@brixmail.com
Lic No. 718263D
Nice to have
• Fb and insta icons. @velmorconstruct
Should not have
• No hammer or tool icons please.

No address line.

```html
<!DOCTYPE html>
<html lang="en">
<head>
<meta charset="utf-8">
<title>Velmor Construct – Business Card</title>
<link href="https://fonts.googleapis.com/css2?family=Montserrat:wght@500&family=Open+Sans:wght@400;500&display=swap" rel="stylesheet">
<style>
  :root {
    --stage-centre: #6a6a6a;
    --stage-edge: #333333;
    --card-dark-top: #1f1f1f;
    --card-dark-bottom: #2c2c2c;
    --card-light: #ffffff;
    --accent: #ee9a3e;
    --ink: #2a2a2a;
    --ink-on-dark: #ffffff;
  }
  * { margin: 0; padding: 0; box-sizing: border-box; }
  html, body { width: 1200px; height: 472px; overflow: hidden; }
  body {
    position: relative;
    background: radial-gradient(ellipse at 50% 50%, var(--stage-centre) 0%, var(--stage-edge) 75%);
    font-family: "Open Sans", sans-serif;
  }
  .card {
    position: absolute;
    top: 94px;
    width: 481px;
    height: 275px;
    border-radius: 14px;
    overflow: hidden;
  }
  .card--front {
    left: 81px;
    background: linear-gradient(135deg, var(--card-dark-top), var(--card-dark-bottom));
  }
  .card--back {
    left: 632px;
    background: var(--card-light);
    color: var(--ink);
  }
  .front-brand {
    position: absolute;
    left: 95px;
    top: 101px;
    display: flex;
    align-items: center;
    gap: 20px;
  }
  .brand-square {
    width: 56px;
    height: 56px;
    border: 2px solid var(--accent);
  }
  .front-wordmark {
    font-family: "Montserrat", sans-serif;
    font-weight: 500;
    font-size: 37px;
    letter-spacing: 0.3em;
    color: var(--ink-on-dark);
  }
  .back-brand {
    position: absolute;
    left: 38px;
    top: 88px;
    width: 125px;
    display: flex;
    flex-direction: column;
    align-items: center;
    gap: 12px;
  }
  .back-brand .brand-square { width: 74px; height: 74px; border-width: 3px; }
  .back-wordmark {
    font-size: 20px;
    font-weight: 500;
    letter-spacing: 0.12em;
    color: var(--accent);
  }
  .licence {
    position: absolute;
    right: 46px;
    top: 115px;
    top: 115px;
    font-size: 14px;
    top: 115px;
  }
  .licence { top: 21px; }
  .details {
    position: absolute;
    left: 214px;
    top: 99px;
  }
  .company-name {
    font-size: 23px;
    line-height: 26px;
    color: var(--accent);
    letter-spacing: -0.01em;
  }
  .company-service {
    font-size: 17px;
    line-height: 22px;
  }
  .person-name {
    margin-top: 10px;
    font-size: 23px;
    line-height: 26px;
    color: var(--accent);
  }
  .contact-list {
    list-style: none;
    margin-top: 10px;
    font-size: 14.5px;
  }
  .contact-list li {
    display: flex;
    align-items: center;
    height: 18.5px;
  }
  .contact-icon {
    width: 13px;
    height: 13px;
    margin-right: 8px;
    flex: none;
  }
  .contact-icon--square { background: var(--accent); width: 11px; height: 11px; margin: 0 9px 0 1px; }
</style>
</head>
<body>
  <section class="card card--front" aria-label="Card front">
    <div class="front-brand">
      <span class="brand-square" aria-hidden="true"></span>
      <span class="front-wordmark">VELMOR.</span>
    </div>
  </section>

  <section class="card card--back" aria-label="Card back">
    <div class="back-brand">
      <span class="brand-square" aria-hidden="true"></span>
      <span class="back-wordmark">VELMOR</span>
    </div>
    <p class="licence">Lic No. 718263D</p>
    <div class="details">
      <h1 class="company-name">VELMOR CONSTRUCT</h1>
      <p class="company-service">Carpentry &amp; Building Service</p>
      <h2 class="person-name">Nilo Petrakis</h2>
      <ul class="contact-list">
        <li>
          <svg class="contact-icon" viewBox="0 0 13 13" aria-hidden="true">
            <rect x="3" y="0.8" width="7" height="11.4" rx="1.5" fill="none" stroke="var(--accent)" stroke-width="1.4"/>
            <circle cx="6.5" cy="10" r="0.8" fill="var(--accent)"/>
          </svg>
          0481236574
        </li>
        <li>
          <svg class="contact-icon" viewBox="0 0 13 13" aria-hidden="true">
            <rect x="0.5" y="3" width="12" height="8" fill="var(--accent)"/>
            <path d="M0.5 3 L6.5 7.5 L12.5 3" fill="none" stroke="#fff" stroke-width="1"/>
          </svg>
          Velmorconstruct@brixmail.com
        </li>
        <li><span class="contact-icon contact-icon--square" aria-hidden="true"></span>@velmorconstruct</li>
        <li><span class="contact-icon contact-icon--square" aria-hidden="true"></span>@velmorconstruct</li>
      </ul>
    </div>
  </section>
</body>
</html>
```